Security Guard company needs new procedure template to wow potential clients in tender submissions

We need an update to our procedure template that will look very professional and modern. We have many procedures so this template must be editable so the content can be adjusted by us depending on the procedure.
A smart and modern professional front page with editable title etc.
A professional and modern page template for the body of the procedure.

We wish to copy and paste our word document onto this template and be able to use it easily.

I have attached our logo and example of a procedure we have.

Font styles to use
Sans Serif

Requirements
Must have
• Ability for me to edit text and add new sections to the document.
Use as a template for multiple procedures.

```html
<!DOCTYPE html>
<html lang="en">
<head>
<meta charset="utf-8">
<title>HSE Management System – Procedure Page</title>
<link href="https://fonts.googleapis.com/css2?family=Source+Sans+3:wght@400;600;700&display=swap" rel="stylesheet">
<style>
  :root{
    --bg:#e9e9e9;
    --paper:#f7f7f6;
    --red:#c8202f;
    --red-soft:#b0434a;
    --ink:#2f3336;
    --text:#2b2b2b;
    --grey:#9a9a9a;
    --grey-light:#d9d9d9;
    --tan:#d9b08c;
  }
  *{box-sizing:border-box;margin:0;padding:0}
  html,body{width:1200px;height:795px;overflow:hidden;background:var(--bg);
    font-family:"Source Sans 3",Arial,sans-serif;color:var(--text)}
  .page{position:absolute;left:326px;top:10px;width:548px;height:775px;
    background:var(--paper);box-shadow:0 6px 24px rgba(0,0,0,.12)}
  .brand{position:absolute;top:40px;left:0;width:100%;display:flex;justify-content:center;align-items:center;gap:8px}
  .brand-dot{width:14px;height:14px;border-radius:50%;background:var(--red)}
  .brand-name{font-size:17px;font-weight:600;color:var(--red);letter-spacing:.5px}
  .section-band{position:absolute;left:26px;top:128px;width:232px;height:26px;background:var(--red);
    color:#fff;font-weight:700;font-size:15px;line-height:26px;padding-left:14px;white-space:nowrap}
  .section-band .num{margin-right:22px}
  .cycle{position:absolute;left:0;top:100px}
  .cycle text{font-family:"Source Sans 3",Arial,sans-serif}
  .node-label{font-size:9px;fill:var(--ink);font-variant:small-caps;letter-spacing:.3px}
  .centre-brand{font-size:9.5px;font-weight:600;fill:var(--red)}
  .intro{position:absolute;left:64px;top:470px;width:430px;font-size:12.6px;line-height:1.55;text-align:justify}
  .doc-ref{position:absolute;right:40px;bottom:34px;font-size:9px;color:var(--ink)}
  .doc-ref .sep{margin:0 6px}
  .edge{position:absolute;left:0;bottom:0;width:100%;height:7px;display:flex}
  .edge-red{width:42%;background:var(--red)}
  .edge-ink{flex:1;background:var(--ink)}
</style>
</head>
<body>
<main class="page">
  <header class="brand">
    <span class="brand-dot"></span>
    <span class="brand-name">Northgate Protective Group</span>
  </header>

  <h2 class="section-band"><span class="num">4.</span>HSE Management System</h2>

  <svg class="cycle" width="548" height="360" viewBox="0 0 548 360" aria-label="HSE management system cycle">
    <defs>
      <filter id="soft" x="-30%" y="-30%" width="160%" height="160%">
        <feDropShadow dx="0" dy="3" stdDeviation="4" flood-opacity=".18"/>
      </filter>
      <linearGradient id="trainRing" x1="0" y1="0" x2="1" y2="1">
        <stop offset="0" stop-color="#c9585d"/><stop offset="1" stop-color="#9e2b33"/>
      </linearGradient>
    </defs>

    <!-- orbit around the centre -->
    <path d="M247.8 79.2 A82 82 0 0 1 342.8 145.8" fill="none" stroke="var(--grey)" stroke-width="2"/>
    <path d="M342.8 145.8 A82 82 0 0 1 314.7 222.8" fill="none" stroke="var(--ink)" stroke-width="2"/>
    <path d="M314.7 222.8 A82 82 0 0 1 234 237" fill="none" stroke="var(--red)" stroke-width="3"/>
    <path d="M234 237 A82 82 0 0 1 180.3 167.1" fill="none" stroke="var(--tan)" stroke-width="3"/>
    <circle cx="180.3" cy="167.1" r="3" fill="var(--red)"/>

    <!-- centre -->
    <circle cx="262" cy="160" r="58" fill="#fff" filter="url(#soft)"/>
    <circle cx="262" cy="160" r="51" fill="#f1f1f1"/>
    <text class="centre-brand" x="262" y="140" text-anchor="middle">Northgate</text>
    <text class="centre-brand" x="262" y="152" text-anchor="middle">Protective Group</text>
    <text class="node-label" x="262" y="172" text-anchor="middle" font-size="10.5">HSE Management</text>
    <text class="node-label" x="262" y="185" text-anchor="middle" font-size="10.5">System</text>

    <!-- monitoring -->
    <circle cx="327" cy="47" r="36" fill="#fff" stroke="var(--grey)" stroke-width="8" filter="url(#soft)"/>
    <circle cx="327" cy="47" r="15" fill="var(--grey-light)" role="img" aria-label="Monitoring icon"/>
    <circle cx="367" cy="38" r="3" fill="var(--grey)"/>
    <text class="node-label" x="376" y="30">Monitoring</text>
    <text class="node-label" x="376" y="41">Supervision</text>
    <text class="node-label" x="376" y="52">Support</text>

    <!-- leadership -->
    <circle cx="390" cy="183" r="36" fill="#fff" stroke="var(--ink)" stroke-width="8" filter="url(#soft)"/>
    <circle cx="390" cy="183" r="15" fill="#e6c1b8" role="img" aria-label="Leadership icon"/>
    <circle cx="430" cy="172" r="3" fill="var(--ink)"/>
    <text class="node-label" x="439" y="165">Leadership &amp;</text>
    <text class="node-label" x="439" y="176">Commitment to</text>
    <text class="node-label" x="439" y="187">Health &amp; Safety</text>

    <!-- feedback -->
    <circle cx="290" cy="284" r="36" fill="#fff" stroke="var(--red)" stroke-width="8" filter="url(#soft)"/>
    <circle cx="290" cy="284" r="15" fill="#efd3d5" role="img" aria-label="Feedback icon"/>
    <circle cx="290" cy="324" r="3" fill="var(--red)"/>
    <text class="node-label" x="290" y="337" text-anchor="middle">Feedback</text>
    <text class="node-label" x="290" y="347" text-anchor="middle">Reporting</text>
    <text class="node-label" x="290" y="357" text-anchor="middle">Improvement</text>

    <!-- training -->
    <circle cx="176" cy="262" r="36" fill="#fff" stroke="url(#trainRing)" stroke-width="8" filter="url(#soft)"/>
    <circle cx="176" cy="262" r="15" fill="#ecd2c2" role="img" aria-label="Training icon"/>
    <circle cx="138" cy="282" r="3" fill="var(--red-soft)"/>
    <text class="node-label" x="130" y="300" text-anchor="end">Training</text>
    <text class="node-label" x="130" y="311" text-anchor="end">Developing</text>
    <text class="node-label" x="130" y="322" text-anchor="end">Communication</text>
  </svg>

  <p class="intro">NPG commitment to Health, safety and environmental issues comes from the top of our organization down through management leadership and commitment to best practices in all Health, Safety and environmental aspects of our operations. This commitment is translated into an embedded HSE aware organizational culture through the HSE training and development program and clear communication. The HSE training given to our staff is continuously supported through supervision and monitoring of the implementation of our policies. Feedback and reporting form an integral part of the HSE management system; they are the mechanism from which areas of improvement are highlighted and new initiatives and strategies can be put in place to ensure continuous improvement year by year.</p>

  <footer class="doc-ref">NPG-HSE001 – Health, Safety and Environment Policy<span class="sep">|</span>04</footer>
  <div class="edge"><span class="edge-red"></span><span class="edge-ink"></span></div>
</main>
</body>
</html>
```